Maple Hollow Craft Cannabis Company

We need a one-page website designed for a craft cannabis website called "Maple Hollow is a craft cannabis company" that will provide high-quality strains. It's located on maplehollow in Abbotsford British Columbia on lush green acreage. The facility takes pride in its modern technology bloom rooms to contain a healthy environment for high-quality handcrafted cannabis. We need a design that looks modern yet rustic- please do not add any marijuana leaves- We want the site to look professional as it is for investors. we will be selling products and do need the site to say "Coming soon"
Target Market(s)
investors and customers
Number of Pages Required
1 page
Colors
Designer to choose colors to be used in the design.
Requirements
Must have
- greenery- its a cannabis production site with state of the art technology for growing. from seeds to full production it is a craft site with smaller rooms but high-end quality products. we need a tab that has a purchasing section another one for investors to watch our market trends and a page with our mission/ values and visions-
Nice to have
- showing people/ high end images/ greenspace/ farm (horticulture based)
Should not have
- no marijuana leaves

```html
<!DOCTYPE html>
<html lang="en">
<head>
<meta charset="utf-8">
<title>Maple Hollow Craft Cannabis Company</title>
<link href="https://fonts.googleapis.com/css2?family=Montserrat:wght@400;600;700;800&family=Open+Sans:wght@400;600;700&display=swap" rel="stylesheet">
<style>
:root{
  --wood:#3a2116;
  --wood-dark:#2c1810;
  --paper:#eed6a0;
  --panel:#f8ecd4;
  --card:#fbf3e3;
  --green:#1f7a1f;
  --green-dark:#16621a;
  --ribbon-tail:#3b2418;
  --ink:#1f140e;
  --text:#2b2019;
  --muted:#b59a84;
  --accent:#e8b63a;
  --white:#ffffff;
  --lab-blue:#3d5f86;
  --lab-shelf:#c9c2b6;
}
*{box-sizing:border-box;margin:0;padding:0}
html,body{width:1200px;height:3051px;overflow:hidden}
body{position:relative;background:var(--paper);font-family:"Open Sans",Arial,sans-serif;color:var(--text)}
.abs{position:absolute}

/* header + hero */
.hero{left:0;top:0;width:1200px;height:740px;
  background:
    radial-gradient(ellipse 260px 300px at 900px 330px,rgba(255,255,255,.95),rgba(255,255,255,0) 70%),
    radial-gradient(ellipse 200px 240px at 380px 420px,rgba(250,250,252,.9),rgba(250,250,252,0) 70%),
    radial-gradient(ellipse 120px 200px at 70px 560px,rgba(61,95,134,.75),rgba(61,95,134,0) 70%),
    radial-gradient(ellipse 90px 160px at 440px 560px,rgba(61,95,134,.55),rgba(61,95,134,0) 70%),
    radial-gradient(ellipse 90px 240px at 360px 300px,rgba(120,160,80,.45),rgba(120,160,80,0) 70%),
    linear-gradient(180deg,#e9ecee 0%,#d7dcdf 45%,#c3c8cb 70%,#b9bcbc 100%)}
.hero-shelf{left:0;top:470px;width:520px;height:12px;background:var(--lab-shelf);opacity:.7}
.hero-shelf.two{top:640px}
.topbar{left:0;top:0;width:1200px;height:124px;background:linear-gradient(180deg,#3e2418,#2f1a11)}
.scallop-top{left:0;top:118px;width:1200px;height:16px}
.logo{left:168px;top:34px;font-family:"Montserrat",sans-serif;font-weight:700;font-size:30px;color:var(--white);line-height:34px;display:flex;align-items:center;gap:10px}
.logo .dot{width:14px;height:14px;border-radius:50%;background:var(--white)}
.utility{right:175px;top:26px;display:flex;gap:20px;font-size:11px;color:var(--white)}
.utility span::before{content:"";display:inline-block;width:7px;height:7px;background:var(--white);border-radius:2px;margin-right:5px;vertical-align:0}
.nav{left:548px;top:66px;display:flex;font-family:"Montserrat",sans-serif;font-weight:700;font-size:14px;color:var(--white)}
.nav a{color:inherit;text-decoration:none;margin-right:40px}
.nav a.active{color:#3aa23a}
.hero-title{left:0;top:345px;width:1200px;text-align:center;font-family:"Montserrat",sans-serif;font-weight:800;font-size:52px;color:#141414}
.hero-sub{left:0;top:424px;width:1200px;text-align:center;font-size:21px;line-height:30px;color:#1a1a1a}
.dots{left:510px;top:673px;width:180px;height:3px;display:flex;gap:6px}
.dots i{flex:1;background:rgba(255,255,255,.55)}
.dots i.on{background:#fff}
.torn{left:0;top:690px;width:1200px;height:60px}

/* mission */
.about{left:173px;top:795px;width:850px;height:530px;background:var(--panel);box-shadow:0 2px 6px rgba(0,0,0,.15)}
.polaroid{left:128px;top:878px;width:352px;height:290px;background:#fff;padding:14px;transform:rotate(-6deg);box-shadow:0 4px 10px rgba(0,0,0,.3)}
.polaroid div{width:100%;height:100%;background:linear-gradient(120deg,#6b8a3a,#c9d86a 40%,#e6e2c8 70%,#8aa3b0)}
.about-title{font-family:"Montserrat",sans-serif;font-weight:700;font-size:34px;color:var(--ink)}
.about-text{font-size:12.5px;line-height:26px;color:#2a211b;width:440px}

/* ribbons */
.ribbon{height:72px}
.ribbon .tail{position:absolute;top:10px;right:0;width:80px;height:62px}
.ribbon .body{position:absolute;left:0;top:0;height:72px;background:var(--green);color:#fff;font-family:"Montserrat",sans-serif;font-weight:700;font-size:33px;line-height:72px;text-align:center}
.ribbon .body::before{content:"";position:absolute;left:-36px;top:0;border-right:36px solid var(--green);border-top:36px solid transparent;border-bottom:36px solid transparent}

.intro{left:0;top:1396px;width:1200px;text-align:center;font-size:12.5px;line-height:28px;color:#2a211b}

/* products */
.product{top:1476px;width:203px;height:316px;background:var(--card);border:2px solid #fff;box-shadow:0 1px 4px rgba(0,0,0,.12);text-align:center}
.product .ph{height:170px}
.product h3{font-family:"Montserrat",sans-serif;font-weight:700;font-size:15px;color:var(--ink);margin-top:20px}
.product p{font-size:12px;line-height:18px;margin:6px 18px 0}
.btn{display:inline-block;margin-top:14px;width:90px;height:32px;line-height:32px;border-radius:16px;background:var(--green-dark);color:#fff;font-weight:700;font-size:11px}
.soon{background:linear-gradient(160deg,#3c2a22,#2a1a14);display:flex;align-items:center;justify-content:center;font-family:"Montserrat",sans-serif;font-weight:700;font-size:18px;color:#fff}

/* blog */
.blog{left:173px;top:1906px;width:854px;height:534px;background:var(--panel);box-shadow:0 2px 6px rgba(0,0,0,.15)}
.post{top:1998px;width:257px;height:375px;background:#fffaf0;box-shadow:0 1px 4px rgba(0,0,0,.15)}
.post .ph{height:205px;position:relative}
.date{position:absolute;left:20px;top:20px;width:58px;height:58px;border-radius:50%;background:var(--green);color:#fff;font-family:"Montserrat",sans-serif;font-weight:700;font-size:13px;line-height:16px;text-align:center;padding-top:12px}
.post h3{font-family:"Montserrat",sans-serif;font-weight:700;font-size:16px;color:var(--ink);margin:26px 14px 0}
.post p{font-size:11.5px;line-height:19px;margin:10px 14px 0;color:#2a211b}

/* footer */
.footer{left:0;top:2535px;width:1200px;height:516px;background:var(--wood-dark)}
.scallop-foot{left:0;top:2520px;width:1200px;height:20px}
.news-title{left:0;top:2576px;width:1200px;text-align:center;font-family:"Montserrat",sans-serif;font-weight:700;font-size:33px;color:#fff}
.news-form{left:302px;top:2643px;width:596px;height:52px;background:#4a2f22;border-radius:3px}
.news-form span{position:absolute;left:18px;top:17px;font-size:11px;color:#fff}
.news-form b{position:absolute;left:478px;top:9px;width:104px;height:34px;line-height:34px;border-radius:17px;background:var(--green);color:#fff;text-align:center;font-family:"Montserrat",sans-serif;font-size:13px}
.fcol h4{font-family:"Montserrat",sans-serif;font-weight:600;font-size:15px;color:#fff}
.fcol h4.gold{color:var(--accent)}
.fcol .bar{width:20px;height:3px;background:var(--accent);margin:18px 0 12px}
.fcol li{list-style:none;font-size:11px;line-height:18.5px;color:var(--muted)}
.contact-row{display:flex;gap:10px;font-size:11px;line-height:18px;color:var(--muted);margin-bottom:14px}
.contact-row svg{flex:none;width:16px;height:16px;margin-top:1px}
.rule{left:173px;top:2985px;width:854px;height:1px;background:#5a4034}
.social{top:2998px;width:34px;height:34px;border-radius:50%;border:2px solid #fff;display:flex;align-items:center;justify-content:center}
.social svg{width:16px;height:16px}
.copy{right:173px;top:3008px;font-size:10.5px;color:var(--muted)}
</style>
</head>
<body>

<div class="abs hero" role="img" aria-label="Photo of a lab scientist in a white protective suit and goggles holding a test tube of dried cannabis flower in a laboratory"></div>
<div class="abs hero-shelf"></div>
<div class="abs hero-shelf two"></div>
<div class="abs topbar"></div>
<svg class="abs scallop-top" viewBox="0 0 1200 16" preserveAspectRatio="none"><path d="M0 0 H1200 V6 Q1185 16 1170 6 Q1155 16 1140 6 Q1125 16 1110 6 Q1095 16 1080 6 Q1065 16 1050 6 Q1035 16 1020 6 Q1005 16 990 6 Q975 16 960 6 Q945 16 930 6 Q915 16 900 6 Q885 16 870 6 Q855 16 840 6 Q825 16 810 6 Q795 16 780 6 Q765 16 750 6 Q735 16 720 6 Q705 16 690 6 Q675 16 660 6 Q645 16 630 6 Q615 16 600 6 Q585 16 570 6 Q555 16 540 6 Q525 16 510 6 Q495 16 480 6 Q465 16 450 6 Q435 16 420 6 Q405 16 390 6 Q375 16 360 6 Q345 16 330 6 Q315 16 300 6 Q285 16 270 6 Q255 16 240 6 Q225 16 210 6 Q195 16 180 6 Q165 16 150 6 Q135 16 120 6 Q105 16 90 6 Q75 16 60 6 Q45 16 30 6 Q15 16 0 6Z" fill="#2f1a11"/></svg>

<div class="abs logo"><span class="dot"></span>Maple Hollow</div>
<div class="abs utility"><span>Log in</span><span>Register</span><span>Wishlist</span></div>
<nav class="abs nav"><a class="active" href="#">Home</a><a href="#">Shop</a><a href="#">Investors</a><a href="#">About Us</a><a href="#">News</a><a href="#">Contact</a></nav>

<h1 class="abs hero-title">Welcome! to Maple Hollow</h1>
<p class="abs hero-sub">Sed ut perspiciatis unde omnis iste natus error sit voluptatem<br>accusantium doloremque laudantium, totam rem ap</p>
<div class="abs dots"><i></i><i class="on"></i><i></i></div>

<svg class="abs torn" viewBox="0 0 1200 60" preserveAspectRatio="none"><path d="M0 42 L40 38 L70 46 L120 40 L180 47 L230 41 L300 45 L360 39 L420 46 L500 42 L560 48 L640 41 L700 46 L760 40 L830 47 L900 42 L960 46 L1030 40 L1100 46 L1160 41 L1200 44 V60 H0Z" fill="#eed6a0"/></svg>

<section class="abs about"></section>
<div class="abs polaroid"><div role="img" aria-label="Photo of a test tube of cannabis buds in front of coloured sample tubes"></div></div>
<h2 class="abs about-title" style="left:528px;top:876px">Mission</h2>
<p class="abs about-text" style="left:523px;top:929px">Sed ut perspiciatis unde omnis iste natus error sit voluptatem accusantium doloremque laudantium, totam rem aperiam, eaque ipsa quae ab illo inven tore veritatis et quasi architecto beatae vitae dicta sunt explicabo. Nemo eni m ipsam voluptatem quia voluptas sit aspernatur aut odit au</p>
<h2 class="abs about-title" style="left:528px;top:1063px">Vision</h2>
<p class="abs about-text" style="left:523px;top:1116px">Sed ut perspiciatis unde omnis iste natus error sit voluptatem accusantium doloremque laudantium, totam rem aperiam, eaque ipsa quae ab illo inven tore veritatis et quasi architecto beatae vitae dicta sunt explicabo. Nemo eni m ipsam voluptatem quia voluptas sit aspernatur aut odit au</p>

<div class="abs ribbon" style="left:446px;top:1288px;width:370px">
  <svg class="tail" viewBox="0 0 80 62"><path d="M0 0 H80 L62 31 L80 62 H0Z" fill="#3b2418"/></svg>
  <div class="body" style="width:310px">Our Products</div>
</div>

<p class="abs intro">Sed ut perspiciatis unde omnis iste natus error sit voluptatem accusantium doloremque laudantium,<br>totam rem aperiam, eaque ipsa quae ab illo inventore veritatis et quasi architecto beatae vitae</p>

<article class="abs product" style="left:173px"><div class="ph" role="img" aria-label="Photo of a glass jar spilling cannabis buds" style="background:linear-gradient(135deg,#dfe8d8,#8fa66a 55%,#4f6a2c)"></div><h3>Product Name</h3><p>Sed ut perspiciatis unde nis iste natus error sit volut</p><span class="btn">Buy Now</span></article>
<article class="abs product soon" style="left:391px" role="img" aria-label="Dark photo of apothecary jars behind a coming soon notice">Coming Soon</article>
<article class="abs product" style="left:608px"><div class="ph" role="img" aria-label="Photo of an orange pill bottle with cannabis buds" style="background:linear-gradient(135deg,#f2d7c8,#e08a4a 40%,#7b8a3c 75%,#f0e6de)"></div><h3>Product Name</h3><p>Sed ut perspiciatis unde nis iste natus error sit volut</p><span class="btn">Buy Now</span></article>
<article class="abs product" style="left:824px"><div class="ph" role="img" aria-label="Photo of a tipped amber container with cannabis buds" style="background:linear-gradient(135deg,#dbe4ef,#e0a63c 45%,#6e7f3a 70%,#c9d5e2)"></div><h3>Product Name</h3><p>Sed ut perspiciatis unde nis iste natus error sit volut</p><span class="btn">Buy Now</span></article>

<section class="abs blog"></section>
<div class="abs ribbon" style="left:446px;top:1870px;width:370px">
  <svg class="tail" viewBox="0 0 80 62"><path d="M0 0 H80 L62 31 L80 62 H0Z" fill="#3b2418"/></svg>
  <div class="body" style="width:310px">From our Blog</div>
</div>

<article class="abs post" style="left:195px"><div class="ph" role="img" aria-label="Photo of cannabis buds on a wooden table" style="background:linear-gradient(135deg,#3a2a1c,#8a8a4a 50%,#5b3c22)"><span class="date">Nov<br>22</span></div><h3>Lorem ipsum dolormevol</h3><p>Lorem ipsum dolor sit amet, consectetur adip iscing elit, sed do eiusmod tempor incididunt ut labore et dolore magna aliquat enim ad minim veniam, quis nostrud exercitation ulla</p></article>
<article class="abs post" style="left:471px"><div class="ph" role="img" aria-label="Photo of cannabis buds on a dark green background" style="background:linear-gradient(135deg,#1f3a2a,#5c7a3a 50%,#1a2a20)"><span class="date">Nov<br>22</span></div><h3>Lorem ipsum dolormevol</h3><p>Lorem ipsum dolor sit amet, consectetur adip iscing elit, sed do eiusmod tempor incididunt ut labore et dolore magna aliquat enim ad minim veniam, quis nostrud exercitation ulla</p></article>
<article class="abs post" style="left:747px"><div class="ph" role="img" aria-label="Photo of a gloved hand holding a test tube over a digital network graphic" style="background:linear-gradient(135deg,#1c3a6a,#3f78b8 50%,#14284a)"><span class="date">Nov<br>22</span></div><h3>Lorem ipsum dolormevol</h3><p>Lorem ipsum dolor sit amet, consectetur adip iscing elit, sed do eiusmod tempor incididunt ut labore et dolore magna aliquat enim ad minim veniam, quis nostrud exercitation ulla</p></article>

<svg class="abs scallop-foot" viewBox="0 0 1200 20" preserveAspectRatio="none"><path d="M0 20 V10 Q15 0 30 10 Q45 0 60 10 Q75 0 90 10 Q105 0 120 10 Q135 0 150 10 Q165 0 180 10 Q195 0 210 10 Q225 0 240 10 Q255 0 270 10 Q285 0 300 10 Q315 0 330 10 Q345 0 360 10 Q375 0 390 10 Q405 0 420 10 Q435 0 450 10 Q465 0 480 10 Q495 0 510 10 Q525 0 540 10 Q555 0 570 10 Q585 0 600 10 Q615 0 630 10 Q645 0 660 10 Q675 0 690 10 Q705 0 720 10 Q735 0 750 10 Q765 0 780 10 Q795 0 810 10 Q825 0 840 10 Q855 0 870 10 Q885 0 900 10 Q915 0 930 10 Q945 0 960 10 Q975 0 990 10 Q1005 0 1020 10 Q1035 0 1050 10 Q1065 0 1080 10 Q1095 0 1110 10 Q1125 0 1140 10 Q1155 0 1170 10 Q1185 0 1200 10 V20Z" fill="#2c1810"/></svg>
<footer class="abs footer"></footer>

<h2 class="abs news-title">Sign up for Newsletter</h2>
<div class="abs news-form"><span>Email:</span><b>SIGN UP</b></div>

<div class="abs fcol" style="left:173px;top:2757px;width:200px">
  <h4>Contact</h4><div class="bar"></div>
  <div class="contact-row" style="margin-top:14px"><svg viewBox="0 0 16 16"><circle cx="8" cy="8" r="8" fill="#efe2c4"/><path d="M8 3.5a3 3 0 0 0-3 3c0 2.3 3 6 3 6s3-3.7 3-6a3 3 0 0 0-3-3zm0 4.2a1.2 1.2 0 1 1 0-2.4 1.2 1.2 0 0 1 0 2.4z" fill="#2c1810"/></svg><span>12345 Sample Str, Sample State,<br>Sample city, Sample Country</span></div>
  <div class="contact-row" style="margin-top:20px;margin-bottom:2px"><svg viewBox="0 0 16 16"><circle cx="8" cy="8" r="8" fill="#efe2c4"/><rect x="4" y="5" width="8" height="6" rx="1" fill="#2c1810"/><path d="M4.5 5.6 8 8.4l3.5-2.8" stroke="#efe2c4" stroke-width="1" fill="none"/></svg><span>support@companyname.com</span></div>
  <div class="contact-row"><svg viewBox="0 0 16 16"><circle cx="8" cy="8" r="8" fill="#efe2c4"/><path d="M5.2 4.2l1.6-.4 1 2.2-1 .8a5.5 5.5 0 0 0 2.4 2.4l.8-1 2.2 1-.4 1.6c-3.6.4-7-3-6.6-6.6z" fill="#2c1810"/></svg><span>(+01) 123456789xxx</span></div>
</div>
<div class="abs fcol" style="left:415px;top:2757px"><h4 class="gold">Links</h4><div class="bar" style="margin-bottom:22px"></div><ul><li>Contact us</li><li>About us</li><li>Site map</li><li>Terms &amp; Conditions</li><li>My order</li><li>My credit cart slips</li></ul></div>
<div class="abs fcol" style="left:587px;top:2757px"><h4>Company</h4><div class="bar"></div><ul><li>About Us</li><li>Product Reviews</li><li>Privacy Policy</li><li>Terms &amp; Conditions</li><li>Site Map</li><li>Discount Policies</li><li>Advanced Search</li><li>Affiliate</li></ul></div>
<div class="abs fcol" style="left:757px;top:2757px"><h4>My Account</h4><div class="bar"></div><ul><li>My Account</li><li>Order History</li><li>Wish List</li><li>gifts</li><li>wholesale</li><li>in stores</li><li>help</li></ul></div>
<div class="abs fcol" style="left:914px;top:2757px"><h4>Customer Care</h4><div class="bar"></div><ul><li>Order Info</li><li>Shipping / Tracking Info</li><li>Returns Info</li><li>Request Exchange</li><li>Guarantee</li></ul></div>

<div class="abs rule"></div>
<a class="abs social" style="left:171px" aria-label="Email us"><svg viewBox="0 0 16 16"><rect x="1.5" y="3.5" width="13" height="9" rx="1" fill="none" stroke="#fff" stroke-width="1.4"/><path d="M2 4.5 8 9l6-4.5" fill="none" stroke="#fff" stroke-width="1.4"/></svg></a>
<a class="abs social" style="left:210px" aria-label="Chat with us"><svg viewBox="0 0 16 16"><path d="M2 3h12v8H7l-3 3v-3H2z" fill="none" stroke="#fff" stroke-width="1.4" stroke-linejoin="round"/></svg></a>
<a class="abs social" style="left:248px" aria-label="Share"><svg viewBox="0 0 16 16"><circle cx="4" cy="8" r="2" fill="#fff"/><circle cx="12" cy="3.5" r="2" fill="#fff"/><circle cx="12" cy="12.5" r="2" fill="#fff"/><path d="M4 8l8-4.5M4 8l8 4.5" stroke="#fff" stroke-width="1.3"/></svg></a>
<a class="abs social" style="left:286px" aria-label="Favourites"><svg viewBox="0 0 16 16"><path d="M8 14S1.5 9.8 1.5 5.6A3.2 3.2 0 0 1 8 4a3.2 3.2 0 0 1 6.5 1.6C14.5 9.8 8 14 8 14z" fill="#fff"/></svg></a>
<p class="abs copy">Copyright © 2018 All Rights reserved. Privacy Policy &nbsp; Terms &amp; Conditions</p>

</body>
</html>
```